Political sign design, fonts colors and layout

I am running for Town Council.

My message is done, and *a draft is attached* with the text we wish to use. It says "Elect Dana Velloway" etc. In Maroon and White. I am not a designer, but this is somewhat close to what we are looking for.

I need help with colors and fonts, layout, spacing, and general cleanup.

I'm attaching the town high school logo:

- "B" for Brockmere: with black and white outlines on the fonts
- we want to incorporate the black and white on the fonts
- for the entire text, parts of the text, or best would be a mix

This is for signs printed and placed all over my town.

We need two versions

1. square, 4' by 4' version
2. 36" by 24" version

The smaller version will drop the three bullet pointed text, but otherwise can be identical.

The sign can only use 3 printed colors (due to printing costs.)

1. maroon,
2. white,
3. black.

The maroon should match the maroon from the high school logo attached, which I believe I did in the draft.

We also like the white border around the outside, like in the "scoreboard" design attached.

Thanks for your attention, wish me luck.

Dana

Target Market(s)

SIgns, Political market

Industry/Entity Type

Political

Font styles to use
Sans Serif
Other font styles liked:
• Arial Black, Sans Serif Bold

Requirements
Must have
• maroon background, white font.
• - black borders around fonts where appropriate
• - great spacing
• - great typeface usage
• - clean and crisp political sign, visible while driving.
• - my name "Dana Velloway" much larger like the draft, or the appropriate additional size
• - two versions, one square, and one 36" / 24"
Nice to have
• - nice borders
• - dress it up a bit, using italics and bold fonts, without making it flashy or busy.
Should not have
• Must be easily readable from a car, except for "Paid for by Friends of Dana Velloway" which can be tiny.
• Colors are noted in the description, the "Brockmere Maroon" as the background, white font, and some use of black.

```html
<!DOCTYPE html>
<html lang="en">
<head>
<meta charset="utf-8">
<title>Elect Dana Velloway – Brockmere Council Sign</title>
<link rel="stylesheet" href="https://fonts.googleapis.com/css2?family=Archivo+Black&family=Montserrat:wght@300;400;500;700;800&display=swap">
<style>
  :root {
    --maroon: #731f35;
    --white: #ffffff;
    --black: #000000;
  }
  html, body {
    margin: 0;
    padding: 0;
    width: 1200px;
    height: 1200px;
    overflow: hidden;
    background: var(--maroon);
  }
  .sign { display: block; width: 1200px; height: 1200px; }
  .frame-line { fill: none; stroke: var(--white); }
  .header-panel { fill: var(--white); stroke: var(--black); stroke-width: 4; }
  .office-band { fill: var(--black); }
  .tagline { font-family: "Archivo Black", sans-serif; font-size: 38px; fill: var(--black); }
  .elect { font-family: "Montserrat", sans-serif; font-weight: 400; font-size: 148px; fill: var(--black); }
  .star-black { fill: var(--black); }
  .star-white { fill: var(--white); }
  .name { font-family: "Archivo Black", sans-serif; font-size: 128px; stroke-linejoin: round; }
  .name-outer { fill: var(--black); stroke: var(--black); stroke-width: 22; }
  .name-inner { fill: var(--white); stroke: var(--white); stroke-width: 12; }
  .name-fill { fill: var(--maroon); }
  .office { font-family: "Montserrat", sans-serif; font-size: 38px; fill: var(--white); letter-spacing: 1px; }
  .office .light { font-weight: 300; }
  .office .bold { font-weight: 800; }
  .slogan { font-family: "Montserrat", sans-serif; font-size: 70px; fill: var(--white); stroke: var(--black); stroke-width: 5; paint-order: stroke; stroke-linejoin: round; }
  .slogan .heavy { font-weight: 800; }
  .slogan .light { font-weight: 400; stroke-width: 0; }
  .website { font-family: "Montserrat", sans-serif; font-weight: 400; font-size: 60px; fill: var(--white); }
  .vote { font-family: "Archivo Black", sans-serif; font-size: 112px; fill: var(--white); stroke: var(--black); stroke-width: 12; paint-order: stroke; stroke-linejoin: round; }
  .election-day { font-family: "Archivo Black", sans-serif; font-size: 114px; fill: var(--black); stroke: var(--white); stroke-width: 12; paint-order: stroke; stroke-linejoin: round; }
  .election-day .ordinal { font-size: 62px; }
  .disclaimer { font-family: "Montserrat", sans-serif; font-weight: 400; font-size: 23px; fill: var(--white); }
</style>
</head>
<body>
<svg class="sign" viewBox="0 0 1200 1200" xmlns="http://www.w3.org/2000/svg">
  <defs>
    <path id="star" d="M0,-1 L0.2245,-0.309 L0.951,-0.309 L0.363,0.118 L0.588,0.809 L0,0.382 L-0.588,0.809 L-0.363,0.118 L-0.951,-0.309 L-0.2245,-0.309 Z"/>
  </defs>

  <!-- Outer frame -->
  <rect class="frame-line" x="26" y="26" width="1148" height="1148" stroke-width="6"/>
  <rect class="frame-line" x="38" y="38" width="1124" height="1124" stroke-width="2"/>

  <!-- Header panel -->
  <path class="header-panel" d="M53,78 Q53,53 78,53 H1122 Q1147,53 1147,78 V453 A42 42 0 0 0 1105 495 H95 A42 42 0 0 0 53 453 Z"/>

  <text class="tagline" x="600" y="130" text-anchor="middle">Take back our town!</text>

  <g class="star-black">
    <use href="#star" transform="translate(130,236) scale(38)"/>
    <use href="#star" transform="translate(218,236) scale(38)"/>
    <use href="#star" transform="translate(306,236) scale(38)"/>
    <use href="#star" transform="translate(894,236) scale(38)"/>
    <use href="#star" transform="translate(982,236) scale(38)"/>
    <use href="#star" transform="translate(1070,236) scale(38)"/>
  </g>
  <text class="elect" x="600" y="289" text-anchor="middle">ELECT</text>

  <g class="name">
    <text class="name-outer" x="600" y="442" text-anchor="middle" textLength="1020" lengthAdjust="spacingAndGlyphs">DANA VELLOWAY</text>
    <text class="name-inner" x="600" y="442" text-anchor="middle" textLength="1020" lengthAdjust="spacingAndGlyphs">DANA VELLOWAY</text>
    <text class="name-fill" x="600" y="442" text-anchor="middle" textLength="1020" lengthAdjust="spacingAndGlyphs">DANA VELLOWAY</text>
  </g>

  <!-- Office band -->
  <rect class="office-band" x="94" y="495" width="1012" height="61"/>
  <text class="office" x="600" y="540" text-anchor="middle"><tspan class="light">FOR </tspan><tspan class="bold">BROCKMERE COUNCILMAN</tspan><tspan class="light"> / </tspan><tspan class="bold">TRUSTEE</tspan></text>

  <!-- Slogan -->
  <text class="slogan" x="600" y="668" text-anchor="middle"><tspan class="heavy">Fighting</tspan><tspan class="light"> for </tspan><tspan class="heavy">Brockmere</tspan></text>

  <g class="star-white">
    <use href="#star" transform="translate(173,744) scale(22)"/>
    <use href="#star" transform="translate(226,744) scale(22)"/>
    <use href="#star" transform="translate(279,744) scale(22)"/>
    <use href="#star" transform="translate(921,744) scale(22)"/>
    <use href="#star" transform="translate(974,744) scale(22)"/>
    <use href="#star" transform="translate(1027,744) scale(22)"/>
    <use href="#star" transform="translate(389,880) scale(32)"/>
    <use href="#star" transform="translate(811,880) scale(32)"/>
  </g>
  <text class="website" x="600" y="763" text-anchor="middle" textLength="580" lengthAdjust="spacingAndGlyphs">www.votevelloway.com</text>

  <text class="vote" x="600" y="919" text-anchor="middle">VOTE</text>

  <text class="election-day" x="600" y="1047" text-anchor="middle">NOV. 8<tspan class="ordinal" dy="-44">th</tspan><tspan dy="44"> "ROW A"</tspan></text>

  <text class="disclaimer" x="600" y="1111" text-anchor="middle">Paid for by Friends of Dana</text>
</svg>
</body>
</html>
```